custom carpentry, woodworking and home repair company needs logo design and business card design

Attention: I apologize but I just received notification from my state that I cannot use the company name that I originally submitted (Beyond The Bench). The new name will be Lumbrella We need a company logo and business card design for our new company based in the Hampton Roads area of Virginia. The company name is Lumbrella. The final design should give a first impression of true craftsmanship and attention to detail. We would like the card to include the company name, my name Derek Halloway (owner), phone number (757) 482-3175, website (lumbrella-shop.example) and email address (derek@lumbrella-shop.example). Everything else is up to your discretion. Thanks, have fun, and good luck.

Industry/Entity Type

Business

Contact Information for Business Card

See project description

Logo Text

see project description

Colors

Designer to choose colors to be used in the design.

```html
<!DOCTYPE html>
<html lang="en">
<head>
<meta charset="utf-8">
<title>Lumbrella — Business Card</title>
<link rel="stylesheet" href="https://fonts.googleapis.com/css2?family=Arimo:wght@400;700&family=Open+Sans:wght@400&display=swap">
<style>
  :root {
    --backdrop: #f1f1f1;
    --card-dark: #1b1820;
    --card-light: #efefef;
    --gold: #a8884a;
    --ink: #2a2a33;
    --divider: #9a9a9a;
  }
  * { margin: 0; padding: 0; box-sizing: border-box; }
  html, body {
    width: 1200px; height: 1200px; overflow: hidden;
    background: var(--backdrop);
  }
  .card {
    position: absolute;
    left: 251px;
    width: 765px;
    height: 437px;
  }
  .card--front { top: 98px; background: var(--card-dark); }
  .card--back  { top: 650px; background: var(--card-light); }

  .brand {
    position: absolute;
    display: flex;
    align-items: center;
    gap: 12px;
    font-family: "Open Sans", sans-serif;
    font-weight: 400;
    color: var(--gold);
    letter-spacing: 1px;
    white-space: nowrap;
  }
  .brand__dot { border-radius: 50%; background: var(--gold); flex: none; }
  .card--front .brand {
    left: 50%; top: 50%;
    transform: translate(-50%, -50%);
    font-size: 46px;
  }
  .card--front .brand__dot { width: 22px; height: 22px; }
  .card--back .brand {
    left: 589px; top: 158px;
    transform: translate(-50%, -50%);
    font-size: 28px;
  }
  .card--back .brand__dot { width: 14px; height: 14px; }

  .contact {
    position: absolute;
    right: calc(765px - 297px);
    top: 58px;
    text-align: right;
    font-family: "Arimo", sans-serif;
    color: var(--ink);
  }
  .contact__name {
    font-size: 32px; font-weight: 700;
    line-height: 1; margin-bottom: 40px;
    white-space: nowrap;
  }
  .contact__first { color: var(--gold); }
  .contact__line {
    font-size: 20px; line-height: 1;
    margin-bottom: 20px; white-space: nowrap;
  }
  .divider {
    position: absolute;
    left: 335px; top: 65px;
    width: 1px; height: 177px;
    background: var(--divider);
  }
  .bands { position: absolute; left: 0; top: 360px; }
</style>
</head>
<body>
  <section class="card card--front">
    <div class="brand"><span class="brand__dot"></span>Lumbrella</div>
  </section>

  <section class="card card--back">
    <div class="contact">
      <p class="contact__name"><span class="contact__first">Derek</span> Halloway</p>
      <p class="contact__line">(757) 482-3175</p>
      <p class="contact__line">derek@lumbrella-shop.example</p>
      <p class="contact__line">www.lumbrella-shop.example</p>
    </div>
    <div class="divider"></div>
    <div class="brand"><span class="brand__dot"></span>Lumbrella</div>
    <svg class="bands" width="765" height="23" viewBox="0 0 765 23" aria-hidden="true">
      <polygon points="0,0 243,0 229,23 0,23" fill="var(--gold)"/>
      <polygon points="261,0 765,0 765,23 247,23" fill="var(--card-dark)"/>
    </svg>
  </section>
</body>
</html>
```